Flyer Design Project

Need a DL Size flyer (2 sided) for letter box marketing for our website www.brightwardsecure.com.au

Project Deadline Extended
Reason: Thank you for submitting the designs. We like few of the designs and will request those designers to changes few things to make it more suitable for us. Because of holidays need to extend the deadlines. Thank you.

Industry/Entity Type

Marketing

```html
<!DOCTYPE html>
<html lang="en">
<head>
<meta charset="utf-8">
<title>Brightward Secure – CCTV Packages</title>
<link rel="stylesheet" href="https://fonts.googleapis.com/css2?family=Arimo:wght@400;700&family=Roboto+Condensed:wght@400&display=swap">
<style>
  :root {
    --page-bg: #e9e6e1;
    --paper: #ffffff;
    --blue: #1e58a0;
    --blue-dark: #16467f;
    --blue-edge: #0f3566;
    --ink: #1d1d1d;
    --ink-soft: #3a3a3a;
    --cell-light: #ffffff;
    --cell-shade: #e4e4e4;
    --rule: #d2d2d2;
    --frame: #c9c9c9;
  }
  * { box-sizing: border-box; margin: 0; padding: 0; }
  html, body { width: 1200px; height: 772px; overflow: hidden; }
  body { background: var(--page-bg); font-family: "Arimo", Arial, sans-serif; color: var(--ink); }

  .flyer {
    position: absolute; left: 20px; top: 86px;
    width: 1160px; height: 600px;
    background: var(--paper);
    padding: 14px 14px 0;
    box-shadow: 0 2px 10px rgba(0,0,0,.18);
  }

  .packages {
    display: grid;
    grid-template-columns: repeat(6, 1fr);
    border: 2px solid var(--blue-edge);
    background: var(--blue-edge);
    gap: 0 1px;
  }

  .package { display: flex; flex-direction: column; background: var(--cell-light); }

  .package-head {
    height: 66px;
    background: linear-gradient(#2664ae, var(--blue-dark));
    color: #fff; text-align: center;
    padding-top: 5px;
  }
  .package-name { font-size: 19px; font-weight: 700; line-height: 22px; }
  .package-type { font-size: 13.5px; font-weight: 700; line-height: 15px; }

  .package-photo-cell {
    height: 140px; padding: 6px 6px 4px;
    background: linear-gradient(90deg, #f2f2f2, #fff 50%, #e8e8e8);
  }
  .package-photo {
    width: 100%; height: 100%;
    border: 1px solid var(--frame); border-radius: 5px;
    background: linear-gradient(160deg, #f4f5f7 0%, #cfd4da 55%, #3a3e44 100%);
  }

  .features { list-style: none; }
  .features li {
    height: 30.5px; line-height: 30px; text-align: center;
    font-family: "Roboto Condensed", "Arial Narrow", sans-serif;
    font-size: 12.5px; color: var(--ink-soft);
    border-top: 1px solid var(--rule);
    background: linear-gradient(90deg, #ececec, var(--cell-light) 40%, var(--cell-light) 60%, #e6e6e6);
  }

  .package-price {
    height: 36px; line-height: 36px; text-align: center;
    background: linear-gradient(#2a68b2, var(--blue-dark));
    color: #fff; font-weight: 700; font-size: 18.5px;
  }

  .contact-bar {
    display: flex; justify-content: center; align-items: center; gap: 48px;
    height: 56px; font-size: 20px; color: #333;
  }
  .contact-item { display: flex; align-items: center; gap: 10px; }
  .contact-item svg { fill: #555; }
</style>
</head>
<body>
<main class="flyer">
  <section class="packages">
    <article class="package">
      <header class="package-head"><h2 class="package-name">Package 1</h2><p class="package-type">Standalone DVR System<br>(2 Cameras)</p></header>
      <div class="package-photo-cell"><div class="package-photo" role="img" aria-label="Photo of a monitor, standalone DVR recorder and two dome cameras"></div></div>
      <ul class="features">
        <li>2 X high resolution dome cameras</li><li>1 X 4 channel standalone DVR</li><li>500GB hard drive</li><li>19" LCD monitor</li>
        <li>Remote access from PCs &amp; Phones*</li><li>Easy to use</li><li>1 Year Warranty</li><li>Full system supplied &amp; installed</li>
      </ul>
      <p class="package-price">$1495 + GST*</p>
    </article>
    <article class="package">
      <header class="package-head"><h2 class="package-name">Package 2</h2><p class="package-type">Standalone DVR System<br>(4 Cameras)</p></header>
      <div class="package-photo-cell"><div class="package-photo" role="img" aria-label="Photo of a monitor, standalone DVR recorder and four dome cameras"></div></div>
      <ul class="features">
        <li>4 X high resolution dome cameras</li><li>1 X 4 channel standalone DVR</li><li>500GB hard drive</li><li>19" LCD monitor</li>
        <li>Remote access from PCs &amp; Phones*</li><li>Easy to use</li><li>1 Year Warranty</li><li>Full system supplied &amp; installed</li>
      </ul>
      <p class="package-price">$2195 + GST*</p>
    </article>
    <article class="package">
      <header class="package-head"><h2 class="package-name">Package 3</h2><p class="package-type">Standalone DVR System<br>(8 Cameras)</p></header>
      <div class="package-photo-cell"><div class="package-photo" role="img" aria-label="Photo of a monitor, standalone DVR recorder and eight dome cameras"></div></div>
      <ul class="features">
        <li>8 X high resolution dome cameras</li><li>1 X 8 channel standalone DVR</li><li>1 Terrabyte hard drive</li><li>19" LCD monitor</li>
        <li>Remote access from PCs &amp; Phones*</li><li>Easy to use</li><li>1 Year Warranty</li><li>Full system supplied &amp; installed</li>
      </ul>
      <p class="package-price">$3295 + GST*</p>
    </article>
    <article class="package">
      <header class="package-head"><h2 class="package-name">Package 4</h2><p class="package-type">IP based CCTV System<br>(2 Cameras)</p></header>
      <div class="package-photo-cell"><div class="package-photo" role="img" aria-label="Photo of a PC based NVR with monitor and two IP dome cameras"></div></div>
      <ul class="features">
        <li>2 X 2 Megapixel IP Cameras</li><li>1 X PC based NVR System</li><li>500GB hard drive</li><li>19" LCD monitor</li>
        <li>Remote access from PCs &amp; Phones*</li><li>Easy to use</li><li>1 Year Warranty</li><li>Full system supplied &amp; installed</li>
      </ul>
      <p class="package-price">$1995 + GST*</p>
    </article>
    <article class="package">
      <header class="package-head"><h2 class="package-name">Package 5</h2><p class="package-type">IP based CCTV System<br>(4 Cameras)</p></header>
      <div class="package-photo-cell"><div class="package-photo" role="img" aria-label="Photo of a PC based NVR with monitor and four IP dome cameras"></div></div>
      <ul class="features">
        <li>4 X 2 Megapixel IP Cameras</li><li>1 X PC based NVR System</li><li>1 Terrabyte hard drive</li><li>19" LCD monitor</li>
        <li>Remote access from PCs &amp; Phones*</li><li>Easy to use</li><li>1 Year Warranty</li><li>Full system supplied &amp; installed</li>
      </ul>
      <p class="package-price">$3295 + GST*</p>
    </article>
    <article class="package">
      <header class="package-head"><h2 class="package-name">Package 6</h2><p class="package-type">IP based CCTV System<br>(8 Cameras)</p></header>
      <div class="package-photo-cell"><div class="package-photo" role="img" aria-label="Photo of a PC based NVR with monitor and eight IP dome cameras"></div></div>
      <ul class="features">
        <li>8 X 2 Megapixel IP Cameras</li><li>1 X PC based NVR System</li><li>2 Terrabyte hard drive</li><li>19" LCD monitor</li>
        <li>Remote access from PCs &amp; Phones*</li><li>Easy to use</li><li>1 Year Warranty</li><li>Full system supplied &amp; installed</li>
      </ul>
      <p class="package-price">$4495 + GST*</p>
    </article>
  </section>

  <footer class="contact-bar">
    <p class="contact-item">
      <svg width="26" height="22" viewBox="0 0 26 22" aria-hidden="true"><rect x="1" y="1" width="24" height="15" rx="1.5" fill="none" stroke="#555" stroke-width="2"/><rect x="10" y="16" width="6" height="3"/><rect x="6" y="19" width="14" height="2"/></svg>
      brightwardsecure.com.au
    </p>
    <p class="contact-item">
      <svg width="14" height="22" viewBox="0 0 14 22" aria-hidden="true"><rect x="1" y="1" width="12" height="20" rx="2" fill="none" stroke="#555" stroke-width="2"/><rect x="4" y="4" width="6" height="10"/><circle cx="7" cy="17.5" r="1.3"/></svg>
      02 5550 3817
    </p>
    <p class="contact-item">
      <svg width="30" height="20" viewBox="0 0 30 20" aria-hidden="true"><rect x="1" y="1" width="28" height="18" fill="none" stroke="#555" stroke-width="2"/><path d="M1 1 L15 12 L29 1" fill="none" stroke="#555" stroke-width="2"/></svg>
      hello@brightwardsecure.com.au
    </p>
  </footer>
</main>
</body>
</html>
```